Business Card Design Project for Architecture and Interior Design company

We need a business card design and logo for an architecture and design firm located in Santiago de Chile. It´s a small company, and the name is "Vostiq" ("Vost" from my surname Vostani, and "arq" for arquitectura or architecture. But it would also be nice that the logo comunicates de Word game "Vosta" as beautiful in italian, and "arq" as architecture".
The idea is to give a delicate, elegant and sofisticated, yet fresh image. Would prefer grey black and white colors, but wouldn´t mind to use another additional color.
I allready have a web page www.vostiq.cl, but would like to improve the logo design.
Please contact if any further information is requiered.
Reason: Need a more arquitectural and desing spirit in the cards. Few of them give that idea.

```html
<!DOCTYPE html>
<html lang="es">
<head>
<meta charset="utf-8">
<title>Vostiq — Tarjetas de presentación</title>
<link rel="stylesheet" href="https://fonts.googleapis.com/css2?family=Montserrat:wght@300;400&display=swap">
<style>
  :root {
    --backdrop: #1c1c1c;
    --card-light: #f6f6f6;
    --card-dark: #2b2a29;
    --ink-dark: #2a2a2a;
    --ink-light: #ffffff;
    --rule: #8a8a8a;
  }
  * { margin: 0; padding: 0; box-sizing: border-box; }
  html, body {
    width: 1200px; height: 900px; overflow: hidden;
    background: var(--backdrop);
    font-family: "Montserrat", sans-serif;
  }
  .stage {
    position: relative; width: 1200px; height: 900px;
    display: flex; align-items: center; justify-content: center; gap: 60px;
  }
  .card {
    position: relative; width: 500px; height: 290px; border-radius: 30px;
  }
  .card--front { background: var(--card-light); color: var(--ink-dark); }
  .card--back { background: var(--card-dark); color: var(--ink-light); }

  .wordmark { font-weight: 300; letter-spacing: 0.5px; line-height: 1; }
  .card--front .wordmark {
    position: absolute; left: 70px; top: 82px; font-size: 42px;
  }
  .contact {
    position: absolute; left: 70px; top: 150px;
    display: flex; align-items: stretch; gap: 10px;
  }
  .contact__lines {
    text-align: right; font-size: 12.5px; font-weight: 400; line-height: 1.5;
  }
  .contact__rule { width: 1px; background: var(--rule); }
  .contact__person { font-size: 14px; font-weight: 400; line-height: 1.3; }
  .contact__role { display: block; font-size: 11px; margin-top: 2px; }

  .card--back .brand {
    position: absolute; right: 40px; bottom: 56px; text-align: right;
  }
  .card--back .wordmark { font-size: 62px; }
  .card--back .url {
    display: block; margin-top: 8px; font-size: 13px; letter-spacing: 4.5px;
  }
</style>
</head>
<body>
<main class="stage">
  <section class="card card--front">
    <div class="wordmark">Vostiq</div>
    <div class="contact">
      <div class="contact__lines">
        <div>+56 9 41582703</div>
        <div>mvostani@vostiq.cl</div>
        <div>www.vostiq.cl</div>
      </div>
      <div class="contact__rule"></div>
      <div class="contact__person">
        Mara Vostani Ketel
        <span class="contact__role">Arquitecto</span>
      </div>
    </div>
  </section>
  <section class="card card--back">
    <div class="brand">
      <div class="wordmark">Vostiq</div>
      <span class="url">www.vostiq.cl</span>
    </div>
  </section>
</main>
</body>
</html>
```